Velquor Web Site

We need a new web site for a new company, Velquor Pty Ltd.
The company will provide services around the Brintara Skyhold and Tallowbench Suite products.
The company theme is "Work is what you do, not where you go." We aim to separate the concepts of data and place. Our clients can access their data anywhere, any time.
The design should look modern, international and should include the Brintara Associate logo.
Updates
My existing web site is visible at http://quennelworks.example. I am hoping that a good designer can provide a fresh look for the business.
Three images for "Cloud" uploaded today.
Target Market(s)
Business of all kinds
Industry/Entity Type
It Company
Requirements
Nice to have
- Colors and themes might reflect Brintara look and style.

```html
<!DOCTYPE html>
<html lang="en">
<head>
<meta charset="utf-8">
<title>Velquor</title>
<link rel="stylesheet" href="https://fonts.googleapis.com/css2?family=Source+Sans+3:wght@300;400;600;700&display=swap">
<style>
:root{
  --navy:#0b2e78;
  --band:#0a2f9a;
  --ink:#1d3f6e;
  --text:#333;
  --card:#e3e3e3;
  --sky:#2b76e5;
  --green:#5fae1b;
  --grey-bar:#555;
  --orange:#d9730f;
  --panel:#262626;
  --panel-blue:#2c5ca8;
  --rule:#d2d2d2;
  --top:#e6e6e6;
}
*{box-sizing:border-box;margin:0;padding:0}
html,body{width:1200px;height:910px;overflow:hidden;background:#fff}
body{font-family:"Source Sans 3",Arial,sans-serif;color:var(--text);border-top:5px solid var(--top);position:relative}
.site{position:absolute;left:129px;top:0;width:943px;height:905px}
.brand{position:absolute;left:0;top:22px;display:flex;align-items:center;gap:10px}
.brand-square{width:40px;height:40px;background:var(--navy)}
.brand-name{font-size:32px;font-weight:700;color:var(--navy);letter-spacing:.5px}
.nav{position:absolute;right:36px;top:44px;display:flex;gap:14px;font-size:15px;color:#222}
.nav a{color:#222;text-decoration:none}
.nav a.current{color:var(--navy)}
.nav .sep{color:#888}
.hero{position:absolute;left:0;top:77px;width:943px;height:380px;overflow:hidden}
.hero-photo{position:absolute;inset:0;background:
  radial-gradient(ellipse at 50% 35%,#d9d9d9 0%,#a8a8a8 45%,transparent 70%),
  linear-gradient(180deg,#8c8c8c 0%,#bdbdbd 35%,#6f6f6f 65%,#4a4a4a 100%)}
.hero-title{position:absolute;left:19px;top:50px;color:var(--ink)}
.hero-title h1{font-size:42px;font-weight:600;letter-spacing:-1.5px;line-height:1}
.hero-title p{font-size:28px;font-weight:300;letter-spacing:-.5px;color:#333;margin-top:2px}
.panel{position:absolute;right:33px;top:0;width:252px}
.panel-safe{background:var(--panel);border-top:5px solid var(--panel-blue);height:212px;padding:10px 14px 0 0;text-align:right;color:#fff}
.panel-safe h2{font-size:29px;font-weight:300;margin-bottom:12px}
.panel-safe li{list-style:none;font-size:13px;line-height:18.5px}
.panel-customers{background:rgba(235,235,235,.88);height:110px;text-align:center;padding-top:8px}
.panel-customers h3{font-size:19px;font-weight:400;color:var(--ink)}
.customer-name{display:inline-block;margin-top:18px;font-size:25px;font-weight:700;color:#e8a21a}
.contact-band{position:absolute;left:0;top:457px;width:943px;height:44px;background:var(--band);color:#fff;display:flex;align-items:center;justify-content:space-between;padding:0 24px 0 14px;font-size:24px}
.contact-band span{display:flex;align-items:center;gap:10px}
.cards{position:absolute;left:0;top:519px;width:943px;height:245px}
.card{position:absolute;top:0;width:298px;height:245px;background:var(--card);text-align:center;border-top:5px solid}
.card h2{font-size:24px;font-weight:300;color:var(--ink);margin-top:23px;letter-spacing:-.3px}
.card-cloud{left:0;border-color:var(--green)}
.card-cloud svg{margin-top:14px}
.card-cloud p{font-size:15.5px;line-height:20px;color:#444;margin-top:16px}
.card-skyhold{left:323px;background:var(--sky);border-color:var(--grey-bar);color:#fff}
.card-skyhold h2{color:#fff}
.product-name{font-size:36px;font-weight:400;margin-top:34px;letter-spacing:-.5px}
.card-skyhold p{font-size:15.5px;margin-top:34px}
.card-skyhold a{display:block;color:#fff;text-decoration:none;font-size:16px;font-weight:600;margin-top:4px}
.card-testimonials{left:645px;border-color:var(--orange)}
.card-testimonials blockquote{font-size:13.5px;line-height:21px;color:#333;margin:14px 24px 0}
.card-testimonials cite{display:block;font-style:normal;font-size:19px;color:#222;margin-top:12px}
.card-testimonials small{display:block;font-size:13.5px;color:#444}
.footer{position:absolute;left:0;top:801px;width:943px;border-top:2px solid var(--rule);text-align:center;color:#111}
.footer .address{font-size:16px;margin-top:14px}
.footer .lines{font-size:12px;margin-top:2px}
.footer .lines b{font-weight:700}
.footer .dot{margin:0 10px}
.footer .copy{font-size:11px;margin-top:19px}
</style>
</head>
<body>
<div class="site">
  <header>
    <div class="brand"><span class="brand-square"></span><span class="brand-name">VELQUOR</span></div>
    <nav class="nav"><a class="current" href="#">Home</a><span class="sep">|</span><a href="#">Cloud Services</a></nav>
  </header>

  <section class="hero">
    <div class="hero-photo" role="img" aria-label="Photo of a woman working on a laptop while sitting on grey rocks under a cloudy sky"></div>
    <div class="hero-title">
      <h1>Work is what you do,</h1>
      <p>not where you go.</p>
    </div>
    <aside class="panel">
      <div class="panel-safe">
        <h2>Safe and Secure</h2>
        <ul>
          <li>Work is what you do, not where you do it</li>
          <li>Access your files, anywhere, any time</li>
          <li>Use the best skills, whereever they are</li>
          <li>Activate Brintara's Cloud services</li>
          <li>Tallowbench Suite is anywhere you want it to be</li>
          <li>Available around the clock</li>
        </ul>
      </div>
      <div class="panel-customers">
        <h3>Our Customers</h3>
        <span class="customer-name">Harlowe Marine</span>
      </div>
    </aside>
  </section>

  <div class="contact-band">
    <span>
      <svg width="20" height="22" viewBox="0 0 20 22" aria-hidden="true"><path d="M5 1 L8 6 L6 8.5 C7 12 9 15 12 16.5 L14.5 14.5 L19 18 L16.5 21 C9 21 2 12 2 4 Z" fill="#fff"/></svg>
      08 5550 1427
    </span>
    <span>
      <svg width="24" height="16" viewBox="0 0 24 16" aria-hidden="true"><rect x="1" y="1" width="22" height="14" fill="none" stroke="#fff" stroke-width="2"/><path d="M1 1 L12 9 L23 1" fill="none" stroke="#fff" stroke-width="2"/></svg>
      service@velquor.example
    </span>
  </div>

  <section class="cards">
    <article class="card card-cloud">
      <h2>Cloud Data Anywhere</h2>
      <svg width="144" height="86" viewBox="0 0 144 86" aria-hidden="true">
        <path d="M20 70 C2 70 2 44 22 42 C22 18 52 10 64 28 C74 16 96 22 94 42 C110 42 112 70 94 70 Z" fill="#1747a6"/>
        <path d="M44 82 C26 82 26 58 46 56 C46 34 76 26 88 44 C98 32 120 38 118 56 C134 56 136 82 118 82 Z" fill="#1747a6" stroke="#e3e3e3" stroke-width="4"/>
      </svg>
      <p>We help your business and your people<br>work anywhere, any time</p>
    </article>
    <article class="card card-skyhold">
      <h2>Brintara Skyhold</h2>
      <div class="product-name">Nimbusvault</div>
      <p>Worldwide data at your fingertips</p>
      <a href="#">Read More</a>
    </article>
    <article class="card card-testimonials">
      <h2>Testimonials</h2>
      <blockquote>"You are a legend. We have an audit in progress today and I was able to illustrate a "Live" recovery. Thank you for service above and beyond the call of duty. We really appreciate that."</blockquote>
      <cite>Owen Carrick</cite>
      <small>Keystone Planning</small>
    </article>
  </section>

  <footer class="footer">
    <p class="address">PO Box 418, Karrowvale, Western Australia, 6951</p>
    <p class="lines"><b>Telephone:</b>&nbsp; 08 5550 1427<span class="dot">•</span><b>Email Information and Support:</b> service@velquor.example</p>
    <p class="copy">Copyright © 2013 Velquor. All Rights Reserved.</p>
  </footer>
</div>
</body>
</html>
```